Valentine's Day menu

Our establishment on 17, (bar - brasserie - wine bar); Offers a menu for Valentine's Day, one that will be on site and another in delivery.

Menu on site:

Starter: Oysters, warm champagne flambé

Dish: Grilled tournedos, braised endives and Jerusalem artichokes
Ranger Sauce
Sole meunière, lemon sauce, steamed potatoes, rice

Dessert: Tiramisu with red fruits - Flambéed Crêpe Suzette

Menu at 29.90€

Delivery menu: Raclette platter with Savoy cheeses - Pierrade platter and fresh vegetables.
Half-bottle of VERMELLE BLANCS DE BLANS.

Please use the Valentine's Day theme, use our logo and colors (attached). The goal is to get as many reservations as possible.

Reservation required at: 06 52 87 30 19
17
11 rue Honorine Vastel 48210 VALBOURG

I remain at your disposal.

- Rate ; 45€ / Person

```html
<!DOCTYPE html>
<html lang="en">
<head>
<meta charset="utf-8">
<title>Le Dix-Sept – Valentine's Day Menu</title>
<link rel="stylesheet" href="https://fonts.googleapis.com/css2?family=Roboto+Slab:wght@400;700;800&family=Roboto:wght@400;500&display=swap">
<style>
  :root {
    --backdrop: #e7e4e0;
    --paper: #ffffff;
    --paper-tint: #f1edf4;
    --brown-dark: #5e320f;
    --brown: #7d4516;
    --brown-light: #94561d;
    --gold: #d99a1f;
    --gold-text: #c0882a;
    --heading-yellow: #f4c531;
    --ink: #2a1a10;
    --accent-brown: #8c4a14;
    --ribbon-red: #d0141e;
    --silver: #cfd1d4;
  }
  * { box-sizing: border-box; margin: 0; padding: 0; }
  html, body { width: 1200px; height: 800px; overflow: hidden; }
  body { background: var(--backdrop); position: relative; font-family: "Roboto", sans-serif; }

  .flyer {
    position: absolute; left: 330px; top: 18px; width: 540px; height: 764px;
    background: var(--paper); overflow: hidden;
    box-shadow: 0 6px 18px rgba(0,0,0,.18);
  }
  .info-column {
    position: absolute; left: 0; top: 0; width: 226px; height: 100%;
    background: linear-gradient(180deg, var(--paper-tint) 0%, var(--paper) 60%);
  }
  .menu-panel {
    position: absolute; left: 226px; top: 0; width: 314px; height: 100%;
    background: radial-gradient(circle at 70% 40%, var(--brown-light) 0%, var(--brown) 45%, var(--brown-dark) 100%);
  }
  .menu-banner {
    position: absolute; left: 196px; top: 40px; width: 344px; height: 54px;
    background: var(--gold); border-radius: 10px 0 0 10px;
    display: flex; align-items: center; padding-left: 44px;
    font-family: "Roboto Slab", serif; font-weight: 800; font-size: 29px;
    color: var(--brown-dark); letter-spacing: .5px; white-space: nowrap;
  }

  .brand { position: absolute; left: 16px; top: 150px; width: 200px; text-align: center; }
  .brand-mark {
    width: 64px; height: 64px; border-radius: 50%;
    border: 2px solid var(--gold-text); margin: 0 auto 12px;
  }
  .brand-name {
    font-family: "Roboto Slab", serif; font-weight: 700; font-size: 30px;
    color: var(--gold-text); line-height: 1.05; letter-spacing: 1px; white-space: nowrap;
  }
  .brand-tagline { margin-top: 8px; font-size: 6.5px; color: var(--ink); letter-spacing: .2px; white-space: nowrap; }

  .reservation { position: absolute; left: 22px; top: 330px; width: 196px; }
  .reservation-title {
    font-family: "Roboto Slab", serif; font-weight: 800; font-size: 12.5px;
    color: var(--accent-brown); margin-bottom: 8px; white-space: nowrap;
  }
  .contact-line { display: flex; gap: 7px; font-size: 12px; color: var(--ink); line-height: 1.3; margin-bottom: 6px; }
  .contact-line svg { flex: 0 0 14px; margin-top: 1px; }

  .closing { position: absolute; left: 22px; top: 430px; width: 196px; font-family: "Roboto Slab", serif; }
  .closing-note { font-size: 13px; font-weight: 700; color: var(--ink); margin-bottom: 6px; white-space: nowrap; }
  .rate { font-size: 15px; font-weight: 800; color: var(--accent-brown); white-space: nowrap; }
  .rate span { color: var(--ink); }

  .table-photo {
    position: absolute; left: 0; top: 520px; width: 226px; height: 244px;
    background: linear-gradient(160deg, var(--paper) 0%, var(--silver) 55%, #e9b9bb 100%);
  }

  .menu-list { position: absolute; left: 236px; top: 110px; width: 296px; }
  .course { display: flex; gap: 10px; margin-bottom: 16px; }
  .course-icon {
    flex: 0 0 34px; height: 34px; border-radius: 50%;
    background: var(--paper); border: 2px solid var(--gold);
    display: flex; align-items: center; justify-content: center; margin-top: 6px;
  }
  .course-title {
    font-family: "Roboto Slab", serif; font-weight: 800; font-size: 18px;
    color: var(--heading-yellow); line-height: 1.15;
  }
  .course-text { font-size: 12.5px; color: var(--paper); line-height: 1.35; }

  .price-badge {
    position: absolute; left: 402px; top: 470px; width: 122px; height: 122px;
    border-radius: 50%; background: var(--paper); border: 5px solid var(--brown);
    outline: 3px solid var(--paper);
    display: flex; flex-direction: column; align-items: center; justify-content: center;
    font-family: "Roboto Slab", serif; font-weight: 800; color: var(--brown-dark);
  }
  .price-badge .label { font-size: 15px; }
  .price-badge .amount { font-size: 27px; line-height: 1; }

  .ribbon {
    position: absolute; left: 226px; top: 620px; width: 314px; height: 144px;
    background: linear-gradient(200deg, transparent 0%, rgba(208,20,30,.55) 45%, var(--ribbon-red) 100%);
  }
</style>
</head>
<body>
  <main class="flyer">
    <section class="info-column">
      <div class="brand">
        <div class="brand-mark"></div>
        <div class="brand-name">LE<br>DIX-SEPT</div>
        <div class="brand-tagline">BAR BRASSERIE - COCKTAILS - BIÈRE - CHAMPAGNE - VINS</div>
      </div>

      <div class="reservation">
        <div class="reservation-title">RESERVATION REQUIRED AT:</div>
        <div class="contact-line">
          <svg width="14" height="14" viewBox="0 0 14 14" aria-hidden="true">
            <circle cx="7" cy="7" r="7" fill="#8c4a14"/>
            <path d="M4.5 3.5l1.5 0 .6 2-1 .8a5 5 0 0 0 2.2 2.2l.8-1 2 .6v1.5c-3.5.3-6.4-2.6-6.1-6.1z" fill="#fff"/>
          </svg>
          <span>06 52 87 30 19</span>
        </div>
        <div class="contact-line">
          <svg width="14" height="14" viewBox="0 0 14 14" aria-hidden="true">
            <circle cx="7" cy="7" r="7" fill="#8c4a14"/>
            <path d="M7 3a2.6 2.6 0 0 0-2.6 2.6C4.4 7.6 7 11 7 11s2.6-3.4 2.6-5.4A2.6 2.6 0 0 0 7 3z" fill="#fff"/>
            <circle cx="7" cy="5.6" r="1" fill="#8c4a14"/>
          </svg>
          <span>11 rue Honorine Vastel<br>48210 VALBOURG</span>
        </div>
      </div>

      <div class="closing">
        <div class="closing-note">I remain at your disposal.</div>
        <div class="rate">RATE: <span>45€ / Person</span></div>
      </div>

      <div class="table-photo" role="img" aria-label="Photo of a silver spoon, knife and fork tied together with a red satin ribbon, with small red hearts"></div>
    </section>

    <section class="menu-panel"></section>
    <div class="ribbon" role="img" aria-label="Red satin ribbon curling across the bottom with small red hearts and golden sparkles"></div>

    <div class="menu-banner">MENU ON SITE:</div>

    <div class="menu-list">
      <div class="course">
        <div class="course-icon"></div>
        <div>
          <div class="course-title">STARTER:</div>
          <div class="course-text">Oysters, warm champagne flambé</div>
        </div>
      </div>
      <div class="course">
        <div class="course-icon"></div>
        <div>
          <div class="course-title">DISH:</div>
          <div class="course-text">Grilled tournedos, braised endives and Jerusalem artichokes Ranger Sauce. Sole meunière, lemon sauce, steamed potatoes, rice</div>
        </div>
      </div>
      <div class="course">
        <div class="course-icon"></div>
        <div>
          <div class="course-title">DESSERT:</div>
          <div class="course-text">Tiramisu with red fruits - Flambéed Crêpe Suzette</div>
        </div>
      </div>
      <div class="course">
        <div class="course-icon"></div>
        <div>
          <div class="course-title">DELIVERY MENU:</div>
          <div class="course-text">Raclette platter with Savoy cheeses - Pierrade platter and fresh vegetables. Half-bottle of VERMELLE BLANCS DE BLANS.</div>
        </div>
      </div>
    </div>

    <div class="price-badge">
      <span class="label">MENU AT</span>
      <span class="amount">29.90€</span>
    </div>
  </main>
</body>
</html>
```